Professional, Attractive, Simple Website Needed!!

We completed the design for our logo.

We need a website built out around this.

Here are a couple samples of how we want ours formatted.

http://brvntapower.com

http://www.halvorbeam.com/lp/free-quote?LeadSource=Search%20Engine&ProgramName=webquery&experience=qual&language=en&type=brd&gclid=Xq7RTPwmEYKDLAvUHbsNQkfPZrTcGwnJuoVbXeLqHmRYdAsWtPkMcNfBYgzTrUoQJhEdWvKpYaLsZbCmNDgQwTxAoKpXbT_qkR

http://morvalo.co

Reason: Extending this deadline due to our delay in providing designers with content for each page. This is coming in next 24 hours.

Reason: Due to scheduling conflicts and extended travel delays related to Puerto Rico, the deadline has been extended. Your patience is greatly appreciated.

Reason: Travel and scheduling conflicts have made it impossible to give this project the thorough review it deserves, therefore I am extending the deadline. Thank you for your patience!

Target Market(s)

Home Owners who earn 60k + household annually

Industry/Entity Type

It Professional

Coding

Coded - Design and coding required

Number of Pages Required

5+ page

Font styles to use
Serif

Colors
34a7d8
9bcb3c

Requirements
Must have
• Simple
• Lead form Entry (Ability for visitor to enter Name, number and address for a quote)
• Sleek Design
• Professional
• Testimonials
• Use color Scheme of Design Logo Attached
Nice to have
• Video when site starts
• Like this
• https://www.vidmarrow.com/watch?v=qT8mRpXw2Ka&feature=vidm.ro
Should not have
• Should not include Commercial solar
• Should not include wind power

```html
<!DOCTYPE html>
<html lang="en">
<head>
<meta charset="utf-8">
<title>Brightfield Energy — Go Green, Save Money</title>
<link rel="stylesheet" href="https://fonts.googleapis.com/css2?family=Playfair+Display:ital,wght@0,400;0,700;1,400&family=Roboto:wght@400;500;700&display=swap">
<style>
  :root {
    --page-bg: #f4f4f4;
    --white: #ffffff;
    --brand-blue: #2ba8dc;
    --brand-green: #b5d65c;
    --band-green: #c9e39a;
    --ink: #1d1d1d;
    --muted: #666666;
    --footer-bg: #1c1c1c;
    --footer-text: #cfcfcf;
  }
  * { box-sizing: border-box; margin: 0; padding: 0; }
  html, body { width: 1200px; height: 1000px; overflow: hidden; }
  body {
    background: var(--page-bg);
    font-family: "Roboto", Arial, sans-serif;
    color: var(--ink);
    position: relative;
  }
  .site {
    position: absolute; left: 311px; top: 0;
    width: 578px; height: 982px;
    background: var(--white);
  }
  /* Hero */
  .hero {
    position: absolute; left: 0; top: 0; width: 578px; height: 275px;
    background: linear-gradient(160deg, #8fb7de 0%, #b9d2ea 35%, #3c4a66 55%, #2b3550 75%, #8a5a44 100%);
  }
  .brand {
    position: absolute; left: 20px; top: 26px;
    display: flex; align-items: center; gap: 6px;
    color: var(--white); font-family: "Roboto", sans-serif;
    font-weight: 500; font-size: 9px; letter-spacing: .3px;
  }
  .brand-dot { width: 18px; height: 18px; border: 2px solid var(--white); border-radius: 50%; flex: none; }
  .nav {
    position: absolute; right: 8px; top: 11px;
    display: flex; gap: 8px; list-style: none;
    font-size: 7.5px; font-weight: 700; color: var(--white);
  }
  .nav .phone { color: var(--brand-green); font-weight: 400; margin-left: 6px; }
  .play-button {
    position: absolute; left: 276px; top: 124px;
    width: 26px; height: 26px; border-radius: 50%;
    background: rgba(255,255,255,.55);
  }
  .play-button svg { position: absolute; left: 9px; top: 8px; }
  /* Quote box */
  .quote-box {
    position: absolute; left: 42px; top: 248px; width: 494px; height: 115px;
    background: var(--brand-blue); text-align: center; color: var(--white);
  }
  .quote-box h1 {
    font-family: "Playfair Display", Georgia, serif; font-weight: 700;
    font-size: 17px; margin-top: 21px;
  }
  .quote-box p { font-size: 9.5px; margin-top: 5px; }
  .quote-form { display: flex; justify-content: center; margin-top: 9px; }
  .zip-input {
    width: 176px; height: 21px; border-radius: 11px 0 0 11px;
    background: var(--white); color: #999; font-size: 7px;
    text-align: left; padding: 6px 15px;
  }
  .quote-button {
    width: 86px; height: 21px; border-radius: 0 11px 11px 0;
    background: var(--brand-green); color: var(--ink);
    font-size: 6px; font-weight: 700; letter-spacing: .3px; padding-top: 7px;
  }
  /* Benefits */
  .section-title {
    position: absolute; left: 0; top: 405px; width: 578px; text-align: center;
    font-family: "Playfair Display", Georgia, serif; font-weight: 700; font-size: 17px;
  }
  .benefit { position: absolute; top: 448px; text-align: center; }
  .benefit-photo { height: 156px; }
  .benefit h3 {
    font-family: "Playfair Display", Georgia, serif; font-weight: 700;
    font-size: 12.5px; margin-top: 10px; letter-spacing: .2px;
  }
  .benefit p {
    font-family: "Playfair Display", Georgia, serif; font-size: 7px;
    line-height: 10.5px; color: var(--muted); margin: 7px auto 0; width: 140px;
  }
  .benefit .learn-more {
    display: block; font-size: 5.5px; font-weight: 500; letter-spacing: .4px;
    color: var(--brand-blue); margin-top: 9px;
  }
  .benefit--zero { left: 0; width: 202px; }
  .benefit--zero h3 { margin-top: 13px; }
  .benefit--bills { left: 205px; width: 168px; }
  .benefit--free { left: 376px; width: 202px; }
  .photo-couple { background: linear-gradient(135deg, #efe9e0, #c9a57c 60%, #f3efe8); }
  .photo-plant { background: radial-gradient(circle at 50% 60%, #6b5a38, #17233a 70%); }
  .photo-installer { background: linear-gradient(180deg, #b7d2ea 0%, #dfe9f2 40%, #4c5f8c 70%, #2c3d6b 100%); }
  /* Testimonial */
  .testimonial {
    position: absolute; left: 0; top: 731px; width: 578px; height: 153px;
    background: linear-gradient(100deg, #b6d77a 0%, var(--band-green) 60%, #d6ebb2 100%);
  }
  .client-photo {
    position: absolute; left: 103px; top: 21px; width: 110px; height: 110px;
    border-radius: 50%; background: linear-gradient(160deg, #8a7262, #2a2a30);
  }
  .quote-text {
    position: absolute; left: 244px; top: 41px; width: 230px; text-align: center;
    font-family: "Playfair Display", Georgia, serif; font-style: italic;
    font-size: 13px; line-height: 19px; color: #3d4a30; letter-spacing: .3px;
  }
  .quote-author { display: block; font-family: "Roboto", sans-serif; font-style: normal; font-size: 6px; line-height: 8px; margin-top: 7px; color: #3d4a30; letter-spacing: .3px; }
  .pager { position: absolute; right: 44px; top: 135px; display: flex; gap: 5px; list-style: none; font-size: 5.5px; }
  .pager li { width: 9px; height: 9px; text-align: center; line-height: 9px; }
  .pager .active { border: 1px solid #555; }
  /* Footer */
  .footer {
    position: absolute; left: 0; top: 886px; width: 578px; height: 96px;
    background: var(--footer-bg); color: var(--footer-text); font-size: 6.5px;
  }
  .footer-brand {
    position: absolute; left: 36px; top: 22px; width: 82px;
    display: flex; flex-direction: column; align-items: center; gap: 4px;
    color: var(--brand-blue); font-weight: 500; font-size: 8px; text-align: center;
  }
  .footer-brand .brand-dot { width: 28px; height: 28px; border-color: var(--brand-green); }
  .footer-contact { position: absolute; left: 128px; top: 23px; line-height: 10px; }
  .footer h4 { color: var(--white); font-size: 6.5px; font-weight: 700; margin-bottom: 9px; }
  .footer-contact .phone-line { margin-top: 9px; }
  .footer-social { position: absolute; left: 335px; top: 23px; }
  .social-list { display: flex; gap: 8px; list-style: none; }
  .social-list li { width: 10px; height: 10px; background: #e4e4e4; }
  .copyright {
    position: absolute; left: 311px; top: 986px; width: 578px; text-align: center;
    font-size: 5.5px; color: #777;
  }
</style>
</head>
<body>
  <div class="site">
    <header class="hero" role="img" aria-label="Photo of a brick house roof covered with solar panels under a blue sky">
      <div class="brand"><span class="brand-dot"></span>Brightfield Energy</div>
      <ul class="nav">
        <li>RESIDENTIAL</li><li>BUSINESS</li><li>WHY BRIGHTFIELD</li><li>FAQS</li><li>CONTACT US</li>
        <li class="phone">+440000482913</li>
      </ul>
      <div class="play-button">
        <svg width="9" height="10" viewBox="0 0 9 10"><path d="M0 0 L9 5 L0 10 Z" fill="#555"/></svg>
      </div>
    </header>

    <section class="quote-box">
      <h1>Go Green, Save Money</h1>
      <p>See how much you'll save</p>
      <div class="quote-form">
        <div class="zip-input">Your zip code</div>
        <div class="quote-button">GET A FREE QUOTE</div>
      </div>
    </section>

    <h2 class="section-title">Why Brightfield Energy?</h2>

    <article class="benefit benefit--zero">
      <div class="benefit-photo photo-couple" role="img" aria-label="Photo of a smiling couple on a sofa looking at a tablet"></div>
      <h3>Zero Cost</h3>
      <p>Lorem ipsum dolor sit amet, consectetur adipiscing elit. Sed maximus justo at massa mattis imperdiet.</p>
      <span class="learn-more">LEARN MORE</span>
    </article>
    <article class="benefit benefit--bills">
      <div class="benefit-photo photo-plant" role="img" aria-label="Photo of hands holding soil with a young plant and a light bulb"></div>
      <h3>Lower Energy Bills</h3>
      <p>Lorem ipsum dolor sit amet, consectetur adipiscing elit. Sed maximus justo at massa mattis imperdiet.</p>
      <span class="learn-more">LEARN MORE</span>
    </article>
    <article class="benefit benefit--free">
      <div class="benefit-photo photo-installer" role="img" aria-label="Photo of a technician installing solar panels on a roof"></div>
      <h3>Maintenance Free</h3>
      <p>Lorem ipsum dolor sit amet, consectetur adipiscing elit. Sed maximus justo at massa mattis imperdiet.</p>
      <span class="learn-more">LEARN MORE</span>
    </article>

    <section class="testimonial">
      <div class="client-photo" role="img" aria-label="Round portrait photo of a happy customer couple"></div>
      <blockquote class="quote-text">“Nam sed tincidunt nisi. Nulla a nibh at ante faucibus vulputate eu condimentum erat.”
        <span class="quote-author">John &amp; Jane Doe</span>
      </blockquote>
      <ul class="pager"><li>1</li><li class="active">2</li><li>3</li><li>4</li></ul>
    </section>

    <footer class="footer">
      <div class="footer-brand"><span class="brand-dot"></span>Brightfield Energy</div>
      <div class="footer-contact">
        <h4>BRIGHTFIELD ENERGY</h4>
        <p>Orchard Lane, Millbrook,<br>Northfield, Westshire, NF2 4QT</p>
        <p class="phone-line">+440000482913 | info@brightfieldenergy.co.uk</p>
      </div>
      <div class="footer-social">
        <h4>Keep in touch</h4>
        <ul class="social-list"><li></li><li></li><li></li></ul>
      </div>
    </footer>
  </div>
  <p class="copyright">© 2017 Brightfield Energy. All rights reserved.</p>
</body>
</html>
```